Design logo and business card.

Design and construct logo and card for my business which is an over seeing company of other smaller businesses. The companies name is eleven5 venture alliance. Im open to any ideas but i am looking for a very cool contemporary design with a very prestige feel. The card can be either single or double sided, Thank you and i will look forward to your submissions.

Industry/Entity Type

Business

Requirements
Must have
• Company name, email, website, telephone, my name. Cool modern look with a prestige feel.

```html
<!DOCTYPE html>
<html lang="en">
<head>
<meta charset="utf-8">
<title>eleven5 venture alliance — Business Card</title>
<link rel="stylesheet" href="https://fonts.googleapis.com/css2?family=Alegreya+Sans:wght@400&display=swap">
<style>
  :root {
    --paper: #ffffff;
    --ink: #000000;
    --panel: #000000;
    --panel-ink: #ffffff;
    --ornament-light: #f3f3f3;
    --ornament-mid: #dadada;
  }
  html, body {
    margin: 0;
    padding: 0;
    width: 1200px;
    height: 686px;
    overflow: hidden;
    background: var(--paper);
  }
  .card {
    position: relative;
    width: 1200px;
    height: 686px;
    background: var(--paper);
    font-family: "Alegreya Sans", sans-serif;
    overflow: hidden;
  }
  .brand-side {
    position: absolute;
    left: 0;
    top: 0;
    width: 757px;
    height: 686px;
  }
  .ornament {
    position: absolute;
    left: 20px;
    top: 0;
    width: 737px;
    height: 686px;
    background: radial-gradient(ellipse at 62% 50%, var(--ornament-mid) 0%, var(--ornament-light) 42%, var(--paper) 72%);
    opacity: 0.5;
  }
  .wordmark {
    margin: 0;
    font-weight: 400;
    color: var(--ink);
  }
  .wordmark-name {
    position: absolute;
    left: 0;
    top: 215px;
    width: 709px;
    text-align: right;
    font-size: 160px;
    line-height: 1;
    letter-spacing: -1px;
    white-space: nowrap;
  }
  .wordmark-tagline {
    position: absolute;
    left: 69px;
    top: 407px;
    font-size: 70px;
    line-height: 1;
    white-space: nowrap;
  }
  .contact-panel {
    position: absolute;
    left: 757px;
    top: 0;
    width: 443px;
    height: 686px;
    background: var(--panel);
    color: var(--panel-ink);
    text-align: center;
  }
  .person-name {
    position: absolute;
    left: 0;
    right: 0;
    top: 190px;
    margin: 0;
    font-size: 70px;
    font-weight: 400;
    line-height: 1;
  }
  .contact-list {
    position: absolute;
    left: 0;
    right: 0;
    top: 390px;
    margin: 0;
    padding: 0;
    list-style: none;
    font-size: 50px;
    line-height: 87px;
    white-space: nowrap;
  }
</style>
</head>
<body>
  <div class="card">
    <section class="brand-side">
      <div class="ornament" role="img" aria-label="Faint grey flourish ornament behind the company name"></div>
      <h1 class="wordmark">
        <span class="wordmark-name">eleven5</span>
        <span class="wordmark-tagline">venture alliance</span>
      </h1>
    </section>
    <section class="contact-panel">
      <h2 class="person-name">Lena Marsh</h2>
      <ul class="contact-list">
        <li class="contact-phone">+34 611 420 587</li>
        <li class="contact-web">e5alliance.com</li>
        <li class="contact-email">info@e5alliance.com</li>
      </ul>
    </section>
  </div>
</body>
</html>
```